Steady Rig Vitals: Truck Smoke Check Company

I need a logo for a truck health company in California called "Steady Rig Vitals". This company does smoke checks for heavy duty diesel trucks under the Western Clean Skies Council (WCSC) called HD I/M tests. I want the brand to feel reliable.

Target Market(s)

California Diesel Trucks. Individual truck drivers and trucking companies.

Industry/Entity Type

Automotive

Contact Information for Business Card

Company Name, Slogan, contact information. marcusbell@steadyrigvitals.example

```html
<!DOCTYPE html>
<html lang="en">
<head>
<meta charset="utf-8">
<title>Steady Rig Vitals — Business Card</title>
<link rel="stylesheet" href="https://fonts.googleapis.com/css2?family=Roboto:wght@300;400;500;700&display=swap">
<style>
  :root {
    --backdrop: #d2d6d6;
    --paper: #f1f1ef;
    --navy: #0f2f5c;
    --sky: #2a9fd0;
    --gold: #e3a21f;
    --ink: #4a4d52;
    --edge: #1c4f9c;
  }
  * { margin: 0; padding: 0; box-sizing: border-box; }
  html, body {
    width: 1200px;
    height: 1049px;
    overflow: hidden;
    background: var(--backdrop);
    font-family: "Roboto", Arial, sans-serif;
  }
  .sheet {
    position: relative;
    width: 1200px;
    height: 1049px;
  }
  .card {
    position: absolute;
    left: 240px;
    width: 720px;
    height: 411px;
    background: var(--paper);
    box-shadow: 0 10px 30px rgba(0,0,0,0.12);
  }
  .card--front { top: 84px; border-bottom: 5px solid var(--edge); }
  .card--back { top: 560px; }

  .brand {
    display: flex;
    flex-direction: column;
    align-items: center;
    gap: 18px;
  }
  .brand__dot {
    border-radius: 50%;
    background: var(--navy);
  }
  .brand__name {
    color: var(--navy);
    font-weight: 500;
    letter-spacing: 0.08em;
    text-transform: uppercase;
    white-space: nowrap;
  }

  .card--front .brand {
    position: absolute;
    inset: 0;
    justify-content: center;
  }
  .card--front .brand__dot { width: 120px; height: 120px; }
  .card--front .brand__name { font-size: 40px; }

  .card--back .brand {
    position: absolute;
    left: 40px;
    top: 110px;
    width: 300px;
  }
  .card--back .brand__dot { width: 80px; height: 80px; }
  .card--back .brand__name { font-size: 24px; }

  .divider {
    position: absolute;
    left: 372px;
    top: 100px;
    width: 2px;
    height: 210px;
    background: var(--gold);
  }

  .contact {
    position: absolute;
    left: 400px;
    top: 100px;
    color: var(--ink);
  }
  .contact__name {
    color: var(--navy);
    font-size: 26px;
    font-weight: 700;
    letter-spacing: 0.02em;
    text-transform: uppercase;
  }
  .contact__role {
    color: var(--sky);
    font-size: 17px;
    font-weight: 300;
    margin-top: 2px;
  }
  .contact__address {
    font-style: normal;
    font-size: 17px;
    line-height: 1.35;
    margin-top: 16px;
  }
  .contact__list {
    list-style: none;
    margin-top: 14px;
    font-size: 17px;
    line-height: 1.35;
  }
  .contact__list li {
    display: flex;
    align-items: center;
    gap: 10px;
  }
  .icon {
    width: 16px;
    height: 16px;
    flex: none;
    fill: var(--sky);
  }
</style>
</head>
<body>
<main class="sheet">

  <section class="card card--front" aria-label="Card front">
    <div class="brand">
      <span class="brand__dot"></span>
      <span class="brand__name">Steady Rig Vitals</span>
    </div>
  </section>

  <section class="card card--back" aria-label="Card back">
    <div class="brand">
      <span class="brand__dot"></span>
      <span class="brand__name">Steady Rig Vitals</span>
    </div>

    <div class="divider"></div>

    <div class="contact">
      <h1 class="contact__name">Dana Whitlow</h1>
      <p class="contact__role">Founder &amp; CEO</p>
      <address class="contact__address">
        48 Harbor Crest Lane,<br>
        Fairview, CA 95010
      </address>
      <ul class="contact__list">
        <li>
          <svg class="icon" viewBox="0 0 16 16" aria-hidden="true"><path d="M3.2 1.5l2.4 0 1 3.2-1.6 1.2c.8 1.8 2.3 3.3 4.1 4.1l1.2-1.6 3.2 1v2.4c0 .8-.7 1.4-1.5 1.4C6.5 13.2 2.8 9.5 1.8 3c0-.8.6-1.5 1.4-1.5z"/></svg>
          555.014.2290
        </li>
        <li>
          <svg class="icon" viewBox="0 0 16 16" aria-hidden="true"><path d="M1 3.5h14v9H1z M1.6 4l6.4 5 6.4-5" fill="none" stroke="#2a9fd0" stroke-width="1.4"/></svg>
          info@steadyrigvitals.example
        </li>
        <li>
          <svg class="icon" viewBox="0 0 16 16" aria-hidden="true"><circle cx="8" cy="8" r="6.5" fill="none" stroke="#2a9fd0" stroke-width="1.4"/><path d="M1.5 8h13M8 1.5c2.2 2 2.2 11 0 13M8 1.5c-2.2 2-2.2 11 0 13" fill="none" stroke="#2a9fd0" stroke-width="1.1"/></svg>
          www.steadyrigvitals.example
        </li>
      </ul>
    </div>
  </section>

</main>
</body>
</html>
```